Business Card for Bright Lantern

Please design a Modern Business card for a Online Marketing Company

Website: http://www.brightlantern-example.com.au

Please do NOT include physical address in design.

Industry/Entity Type

Business

```html
<!DOCTYPE html>
<html lang="en">
<head>
<meta charset="utf-8">
<title>Bright Lantern – Business Card</title>
<link rel="stylesheet" href="https://fonts.googleapis.com/css2?family=Roboto:wght@400;700;900&family=Roboto+Condensed:wght@300;400&display=swap">
<style>
  :root {
    --stage: #8a8a8a;
    --brand-red: #ef4136;
    --deep-red: #c1272d;
    --orange: #f7941d;
    --amber: #fbb040;
    --white: #ffffff;
    --ink: #1a1a1a;
    --soft-white: rgba(255,255,255,0.35);
  }
  * { margin: 0; padding: 0; box-sizing: border-box; }
  html, body { width: 981px; height: 1200px; overflow: hidden; background: var(--stage); }
  .canvas { position: relative; width: 981px; height: 1200px; }

  .card { position: absolute; left: 31px; width: 919px; overflow: hidden; box-shadow: 0 0 0 2px #555; }

  /* Front */
  .card--front { top: 57px; height: 511px; background: var(--white); }
  .front__topbar { position: absolute; left: 0; top: 0; width: 100%; height: 16px;
    background: linear-gradient(90deg, var(--amber), var(--orange) 35%, var(--brand-red)); }
  .brand__mark { position: absolute; left: 50%; top: 140px; width: 130px; height: 130px;
    margin-left: -65px; border-radius: 20px; background: var(--deep-red); }
  .brand__name { position: absolute; left: 0; top: 304px; width: 100%; text-align: center;
    font-family: "Roboto", sans-serif; font-weight: 700; font-size: 48px;
    color: var(--deep-red); letter-spacing: 0.5px; line-height: 1; }
  .brand__tagline { position: absolute; left: 0; top: 350px; width: 100%; text-align: center;
    font-family: "Roboto", sans-serif; font-weight: 700; font-size: 24px; line-height: 1;
    color: var(--ink); }
  .front__footer { position: absolute; left: 0; bottom: 0; width: 100%; height: 65px;
    background: var(--brand-red); display: flex; align-items: center; justify-content: center; }
  .front__url { font-family: "Roboto Condensed", sans-serif; font-size: 22px; color: var(--white); }

  /* Back */
  .card--back { top: 612px; height: 529px; background: var(--brand-red); }
  .social { position: absolute; left: 92px; top: 60px; display: flex; gap: 14px; }
  .social__dot { width: 24px; height: 24px; border-radius: 50%; background: var(--soft-white); }
  .back__decoration { position: absolute; right: 0; top: 0; width: 420px; height: 330px;
    background: radial-gradient(ellipse at 70% 40%, rgba(255,255,255,0.9), rgba(251,176,64,0.55) 55%, rgba(239,65,54,0) 80%); }
  .person { position: absolute; left: 0; top: 175px; }
  .person__name { margin-left: 68px; font-family: "Roboto Condensed", sans-serif; font-weight: 300;
    font-size: 66px; color: var(--white); line-height: 1; }
  .person__role-row { display: flex; align-items: center; margin-top: 8px; }
  .accent-bar { height: 18px; background: linear-gradient(90deg, rgba(251,176,64,0), var(--orange) 40%, var(--amber)); }
  .accent-bar--left { width: 219px; }
  .person__role { margin-left: 16px; font-family: "Roboto Condensed", sans-serif; font-size: 27px; color: var(--white); }
  .contact { position: absolute; left: 235px; top: 353px; font-family: "Roboto Condensed", sans-serif;
    font-size: 31px; color: var(--white); line-height: 40px; }
  .contact__row { display: flex; }
  .contact__label { width: 46px; }
  .accent-bar--right { position: absolute; right: 0; top: 445px; width: 207px; }
</style>
</head>
<body>
<main class="canvas">
  <section class="card card--front" aria-label="Business card front">
    <div class="front__topbar"></div>
    <span class="brand__mark" aria-hidden="true"></span>
    <h1 class="brand__name">BRIGHT LANTERN</h1>
    <p class="brand__tagline">Shine online - Grow online</p>
    <div class="front__footer"><span class="front__url">brightlantern-example.com.au</span></div>
  </section>

  <section class="card card--back" aria-label="Business card back">
    <div class="social" aria-hidden="true">
      <span class="social__dot"></span><span class="social__dot"></span>
      <span class="social__dot"></span><span class="social__dot"></span>
      <span class="social__dot"></span>
    </div>
    <div class="back__decoration" role="img" aria-label="Brand decoration area"></div>
    <div class="person">
      <h2 class="person__name">Sam Rivers</h2>
      <div class="person__role-row">
        <span class="accent-bar accent-bar--left"></span>
        <span class="person__role">Position Title</span>
      </div>
    </div>
    <div class="contact">
      <p class="contact__row"><span class="contact__label">M</span>plan@brightlantern-example.com.au</p>
      <p class="contact__row"><span class="contact__label">W</span>brightlantern-example.com.au</p>
      <p class="contact__row"><span class="contact__label">P</span>0400 000 123</p>
    </div>
    <span class="accent-bar accent-bar--right"></span>
  </section>
</main>
</body>
</html>
```